Nonna's Vellato

I am looking to design a label to be used on a glass jar for packaging a very special spice that has been used in our family for generations. The spice is excellent on meats, burgers, poultry, fish, and more.

The name of the spice is "Nonna's Famous Vellato"

Design should be traditional, with an Italian feel.

Total circumference of the jar is 10"
Height of jar is 4"

Some of the glass should not be covered to reveal color of spice inside.

Target Market(s)

Female 25-75

```html
<!DOCTYPE html>
<html lang="en">
<head>
<meta charset="utf-8">
<title>Nonna's Famous Vellato – Jar Label</title>
<link rel="stylesheet" href="https://fonts.googleapis.com/css2?family=Bowlby+One+SC&display=swap">
<style>
  :root {
    --backdrop: #5a2f17;
    --paper-light: #ede0c2;
    --paper-mid: #d9bf83;
    --paper-edge: #a8783a;
    --paper-yellow: #f0d24a;
    --band-red: #d0634a;
    --band-teal: #4f9a86;
    --band-orange: #ee9a2c;
    --band-orange-hot: #e8692e;
    --ink-brown: #4a1c12;
    --pepper-red: #c8432c;
    --splash-teal: #3fd8c0;
  }
  html, body {
    margin: 0;
    width: 1200px;
    height: 900px;
    overflow: hidden;
    background: var(--backdrop);
  }
  .canvas {
    position: relative;
    width: 1200px;
    height: 900px;
  }
  .jar-label {
    position: absolute;
    left: 145px;
    top: 238px;
    width: 915px;
    height: 382px;
    box-shadow: 0 6px 14px rgba(0, 0, 0, 0.45);
  }
  .jar-label svg { display: block; }
  .label-word {
    font-family: "Bowlby One SC", "Arial Black", sans-serif;
    fill: var(--ink-brown);
  }
</style>
</head>
<body>
<main class="canvas">
  <section class="jar-label" aria-label="Nonna's Famous Vellato spice jar label">
    <svg width="915" height="382" viewBox="0 0 915 382" xmlns="http://www.w3.org/2000/svg">
      <defs>
        <radialGradient id="paper-tone" cx="0.6" cy="0.45" r="0.75">
          <stop offset="0" stop-color="var(--paper-light)"/>
          <stop offset="0.65" stop-color="var(--paper-mid)"/>
          <stop offset="1" stop-color="var(--paper-edge)"/>
        </radialGradient>
        <radialGradient id="yellow-wash" cx="0.22" cy="0.55" r="0.35">
          <stop offset="0" stop-color="var(--paper-yellow)" stop-opacity="0.75"/>
          <stop offset="1" stop-color="var(--paper-yellow)" stop-opacity="0"/>
        </radialGradient>
        <linearGradient id="orange-band-tone" x1="0" y1="1" x2="1" y2="0">
          <stop offset="0" stop-color="var(--band-orange)"/>
          <stop offset="0.55" stop-color="var(--band-orange-hot)"/>
          <stop offset="1" stop-color="var(--band-orange)"/>
        </linearGradient>
        <linearGradient id="pepper-tone" x1="0" y1="1" x2="1" y2="0">
          <stop offset="0" stop-color="var(--pepper-red)"/>
          <stop offset="0.6" stop-color="var(--pepper-red)"/>
          <stop offset="1" stop-color="var(--splash-teal)"/>
        </linearGradient>
      </defs>

      <rect class="paper" width="915" height="382" fill="url(#paper-tone)"/>
      <rect class="paper-wash" width="915" height="382" fill="url(#yellow-wash)"/>

      <polygon class="band band-teal" points="715,0 785,0 360,176 348,136" fill="var(--band-teal)"/>
      <polygon class="band band-orange" points="800,0 915,0 915,52 398,252 378,202" fill="url(#orange-band-tone)"/>
      <polygon class="band band-red" points="173,0 240,0 462,382 392,382" fill="var(--band-red)"/>

      <g class="label-word maker-name" font-size="36">
        <text x="272" y="112" transform="rotate(25 272 100)" text-anchor="middle">N</text>
        <text x="289" y="147" transform="rotate(25 289 135)" text-anchor="middle">O</text>
        <text x="306" y="182" transform="rotate(25 306 170)" text-anchor="middle">N</text>
        <text x="323" y="217" transform="rotate(25 323 205)" text-anchor="middle">N</text>
        <text x="340" y="252" transform="rotate(25 340 240)" text-anchor="middle">A</text>
        <text x="362" y="292" transform="rotate(25 362 280)" text-anchor="middle">'S</text>
      </g>

      <text class="label-word tagline" x="448" y="134" font-size="30" text-anchor="middle" transform="rotate(-22 448 122)">Famous</text>
      <text class="label-word product-name" x="500" y="193" font-size="46" text-anchor="middle" transform="rotate(-21 500 177)">Vellato</text>

      <rect class="pepper-art" x="455" y="190" width="305" height="170" rx="70"
            fill="url(#pepper-tone)" opacity="0.85"
            role="img" aria-label="Watercolour illustration of a red bell pepper with a teal paint splash"/>
    </svg>
  </section>
</main>
</body>
</html>
```